Pillow Company needs Pillow Insert Design

I just started a new pillow line with two pillow types. I have a hotel pillow and an organic pillow. I need two pillow insert signs designed that follow the same layout but are different color types. I want one sign to incorporate silver and white look and another sign to incorporate a green and white look (this one to look organic). They must have the same layout but different colors. I have include examples of what I want it to look like. In addition, I have uploaded the two hi res images for each sign. My logo is uploaded too.

I am open to other concepts and colors as long as it looks modern, clean and upscale. In addition, I need a Made in the USA logo on the pillow insert designs.

I have attached details on sign, images to be used, and examples that I like.

The Pillow Sign Size is 12 inches x 12 inches.

```html
<!DOCTYPE html>
<html lang="en">
<head>
<meta charset="utf-8">
<title>Restwell Alternative Down Pillow Insert</title>
<link href="https://fonts.googleapis.com/css2?family=Allura&family=Arimo:wght@400;700&family=PT+Serif:wght@400;700&display=swap" rel="stylesheet">
<style>
  :root {
    --lime: #72f20e;
    --leaf: #3f9a1c;
    --white: #ffffff;
    --page: #ffffff;
    --ink-green: #62d40a;
  }
  * { margin: 0; padding: 0; box-sizing: border-box; }
  html, body {
    width: 1200px; height: 1000px; overflow: hidden;
    background: var(--page);
  }
  .insert {
    position: absolute; left: 150px; top: 48px;
    width: 900px; height: 900px;
    background: var(--lime);
    box-shadow: 4px 6px 10px rgba(0,0,0,0.45);
  }
  .header {
    position: absolute; left: 0; top: 39px;
    width: 900px; height: 122px;
    background: var(--white);
  }
  .brand {
    position: absolute; left: 70px; top: 56px;
    display: flex; align-items: center; gap: 22px;
  }
  .brand-mark {
    width: 40px; height: 40px; background: var(--lime);
  }
  .brand-name {
    font-family: "Arimo", Arial, sans-serif; font-weight: 700;
    font-size: 44px; color: var(--leaf); letter-spacing: 0.5px;
  }
  .title {
    position: absolute; left: 33px; top: 168px;
    font-family: "Allura", cursive; font-size: 84px;
    color: var(--white); white-space: nowrap; line-height: 1;
  }
  .intro {
    position: absolute; left: 61px; top: 270px; width: 320px;
    font-family: "PT Serif", Georgia, serif; font-weight: 700;
    font-size: 17px; line-height: 22px; color: var(--white);
  }
  .intro p + p { margin-top: 16px; }
  .features {
    position: absolute; left: 70px; top: 428px; width: 300px;
    list-style: none;
    font-family: "Arimo", Arial, sans-serif; font-size: 17px;
    line-height: 21px; color: var(--white);
  }
  .features li { position: relative; padding-left: 38px; }
  .features li::before {
    content: "\2756"; position: absolute; left: 0; top: 0; font-size: 13px;
  }
  .features b { font-weight: 700; }
  .showcase {
    position: absolute; left: 381px; top: 297px;
    width: 517px; height: 567px; background: var(--white);
  }
  .photo {
    position: absolute; left: 0; top: 0; width: 517px; height: 305px;
    background: linear-gradient(180deg, #e4e6e2 0%, #d9d2ca 35%, #efeeec 70%, #ffffff 100%);
  }
  .story {
    position: absolute; left: 75px; top: 327px; width: 400px;
    font-family: "PT Serif", Georgia, serif; font-size: 14px;
    line-height: 19px; color: var(--ink-green); text-align: justify;
  }
  .origin-badge {
    position: absolute; left: 347px; top: 458px;
    width: 123px; height: 82px; background: #c9cdd6;
  }
  .tagline {
    position: absolute; left: 78px; top: 782px;
    height: 48px; display: flex;
    font-family: "PT Serif", Georgia, serif; font-weight: 700;
    font-size: 30px; line-height: 44px; white-space: nowrap;
  }
  .tagline .on-green {
    border: 2px solid var(--white); border-right: none;
    color: var(--white); padding-left: 6px; width: 303px;
  }
  .tagline .on-white {
    border: 2px solid var(--lime); border-left: none;
    color: var(--lime); padding-left: 2px; width: 231px;
  }
  .craft {
    position: absolute; left: 91px; top: 842px;
    font-family: "PT Serif", Georgia, serif; font-weight: 700;
    font-size: 16px; color: var(--white);
  }
</style>
</head>
<body>
  <main class="insert">
    <header class="header">
      <div class="brand" style="top:17px;">
        <span class="brand-mark"></span>
        <span class="brand-name">Restwell</span>
      </div>
    </header>

    <h1 class="title">Alternative Down Pillow</h1>

    <div class="intro">
      <p>This pillow was designed to give yo the most comfortable night's sleep in your life.</p>
      <p>Designed for<br>all types of sleep positions.</p>
    </div>

    <ul class="features">
      <li>Made From the Finest Premium Materials</li>
      <li>Adjusts to your Body Weight and Temperature</li>
      <li>100% Certified Organic Cotton Fabric</li>
      <li>Cool Non-Allergenic, Anti-Microbial, and Hypoallergenic</li>
      <li>Conforms to <b>H</b>ead and <b>N</b>eck for optimal <b>A</b>lignment during <b>S</b>leep</li>
      <li>Mildew Proof and Dust Mite Resistant</li>
      <li>PureCell &reg; toxin free certified foam</li>
    </ul>

    <section class="showcase">
      <div class="photo" role="img" aria-label="Photo of a smiling couple relaxing together in a bright white bed with white pillows and breakfast tray"></div>
      <p class="story">We added revolutionary features from our advanced Super Soft Premium Memory Foam that has an open cell structure design that recovers quickly and does not trap heat to our gel infused polyester fiber to our 100% Certified Organic Cotton Fabric.</p>
      <div class="origin-badge" role="img" aria-label="Made in the USA badge"></div>
    </section>

    <div class="tagline">
      <span class="on-green">Surround Yourself</span><span class="on-white">with the Best!</span>
    </div>

    <p class="craft">Individually Handcrafted</p>
  </main>
</body>
</html>
```